Kindred Stretch - Logo and Business card design

I require a business card design for my Yoga teaching business. I have a design for a logo I would like to use on the card. I would like the logo designed and provided to me separately to the business card in a jpg or tiff high resolution file so I can use this for a web site, letter head, banner in the future.
I am a travelling yoga teacher in Sydney and teach at several gyms, corporates, private clients, schools, yoga studios etc
With the design I have sent thru as a guide,I would like my own text and colours inside this logo. I have a very good idea of how I would like this to look the logo and business name on the front and contact details on the back.

Target Market(s)

Private clients, corporates, schools, gyms, studios, healthcare industry

Industry/Entity Type

Teacher

Requirements
Must have
• What is compulsory is the information sent in the uploaded file
This card must have a feel for the regular yogi to a beginner so that anyone can practice yoga and feel fantastic.
Nice to have
• refer to attached file
Should not have
• I really do not want this to be a boring Yoga card that does not relate to the average person.

```html
<!DOCTYPE html>
<html lang="en">
<head>
<meta charset="utf-8">
<title>Kindred Stretch – Business Card</title>
<link rel="stylesheet" href="https://fonts.googleapis.com/css2?family=Roboto+Condensed:wght@700&family=Roboto:wght@300;400;700&display=swap">
<style>
  :root {
    --magenta: #c8449a;
    --magenta-light: #e27cbc;
    --text-grey: #6a6a6a;
    --card-edge: #c9c9c9;
    --page: #ffffff;
    --tone-green: #3aa64a;
    --tone-orange: #f08a24;
    --tone-blue: #2f8fd0;
    --tone-purple: #8e4aa8;
  }
  * { margin: 0; padding: 0; box-sizing: border-box; }
  html, body {
    width: 1200px;
    height: 1048px;
    overflow: hidden;
    background: var(--page);
  }
  .canvas {
    position: relative;
    width: 1200px;
    height: 1048px;
  }
  .card {
    position: absolute;
    background: #fff;
    border: 2px solid var(--card-edge);
    border-radius: 30px;
    overflow: hidden;
    box-shadow: 0 2px 6px rgba(0,0,0,0.12);
  }
  .card--front {
    left: 22px;
    top: 26px;
    width: 582px;
    height: 998px;
  }
  .card--back {
    left: 626px;
    top: 15px;
    width: 552px;
    height: 1020px;
  }
  .front__artwork {
    position: absolute;
    left: 0;
    top: 152px;
    width: 578px;
    height: 636px;
    border-radius: 40px;
    background:
      radial-gradient(ellipse at 50% 45%, rgba(200,68,154,0.35), rgba(200,68,154,0) 55%),
      linear-gradient(135deg, var(--tone-green) 0%, var(--tone-orange) 30%, var(--magenta) 55%, var(--tone-blue) 80%, var(--tone-purple) 100%);
    opacity: 0.55;
  }
  .front__name {
    position: absolute;
    left: 0;
    width: 100%;
    top: 812px;
    text-align: center;
    font-family: "Roboto Condensed", "Arial Narrow", sans-serif;
    font-weight: 700;
    font-size: 50px;
    letter-spacing: 0.5px;
    color: var(--magenta);
  }
  .back__band {
    position: absolute;
    left: 0;
    width: 100%;
  }
  .back__band--top { top: 0; height: 200px; }
  .back__band--bottom { bottom: 0; height: 200px; }
  .back__details {
    position: absolute;
    left: 0;
    width: 100%;
    top: 292px;
    text-align: center;
    font-family: "Roboto", Arial, sans-serif;
  }
  .contact__name {
    font-weight: 700;
    font-size: 34px;
    color: var(--magenta);
    letter-spacing: 0.5px;
    margin-bottom: 40px;
  }
  .contact__role {
    font-weight: 300;
    font-size: 29px;
    color: var(--text-grey);
    line-height: 47px;
  }
  .contact__abn {
    font-weight: 400;
    font-size: 19px;
    color: var(--text-grey);
    margin-top: 10px;
  }
  .contact__phone,
  .contact__email {
    font-weight: 700;
    font-size: 29px;
    color: var(--magenta);
  }
  .contact__phone { margin-top: 62px; }
  .contact__email { margin-top: 12px; }
</style>
</head>
<body>
<main class="canvas">
  <section class="card card--front">
    <div class="front__artwork" role="img" aria-label="Seated meditating figure formed from colourful yoga words such as focus, energy, balance and harmony"></div>
    <h1 class="front__name">KINDRED STRETCH</h1>
  </section>

  <section class="card card--back">
    <svg class="back__band back__band--top" viewBox="0 0 552 200" preserveAspectRatio="none" aria-hidden="true">
      <path d="M0 0 H552 V118 C430 70 300 105 170 130 C100 143 40 140 0 128 Z" fill="var(--magenta)"/>
      <path d="M0 128 C40 140 100 143 170 130 C300 105 430 70 552 118 V126 C430 82 300 116 170 140 C100 152 40 150 0 138 Z" fill="var(--magenta-light)"/>
    </svg>

    <div class="back__details">
      <h2 class="contact__name">MARA ELLISON</h2>
      <p class="contact__role">Certified Vinyasa Yoga Teacher</p>
      <p class="contact__role">Advanced Core Balance Instructor</p>
      <p class="contact__abn">ABN: 512 708 33164</p>
      <p class="contact__phone">M.: 0400 318 642</p>
      <p class="contact__email">hello@kindredstretch.com</p>
    </div>

    <svg class="back__band back__band--bottom" viewBox="0 0 552 200" preserveAspectRatio="none" aria-hidden="true">
      <path d="M0 70 C120 40 260 55 380 85 C450 102 510 100 552 88 V200 H0 Z" fill="var(--magenta-light)"/>
      <path d="M0 82 C120 52 260 67 380 97 C450 114 510 112 552 100 V200 H0 Z" fill="var(--magenta)"/>
    </svg>
  </section>
</main>
</body>
</html>
```